Door Hanger Design for Electricians Serving Homes

I would like our logo incorporated into the door hanger. We would like a place for a tear off section on the bottom of the hanger with our contact information: K&T Electric - (555) 318-6470 - www.kandtelectric.example - info@kandtelectric.example.
Door Hanger Script
Front Side of the Door Hanger:
[Company Logo]
Need a Reliable Electrician?
Your Local Electrical Expert is Just Around the Corner!
• Quick Response Times
• Affordable Rates
• Quality Workmanship
• Fully Licensed & Insured
• Special Offer:
• 10% OFF Your First Service Call!
Back Side of the Door Hanger:
Don't Let Electrical Issues Keep You in the Dark!
From flickering lights to complete system upgrades, we've got all your
residential electrical needs covered. Our services include:
• Electrical Repairs & Troubleshooting
• Lighting Installation & Upgrades
• Safety Inspections & Code Compliance
• Energy-Efficient Solutions
• 24/7 Emergency Services
• Why Choose Us?
• Friendly, Local Service
• Over 30 Years of Experience
• Satisfaction Guaranteed
• Upfront Pricing
Call Us Today: [Your Phone Number]
Visit Our Website: [Your Website]
Book Your Appointment Now and Claim Your 10% Discount!
Offer valid for new customers on the first visit only. Mention this door hanger when
booking.
[Your Company Name and Contact Information]
Follow Us on Social Media for More Tips and Special Offers!
[Icons for social media platforms: Chatterbook, Snapwave, Peeper, etc.]
Design Tips:
Use bold, clear fonts for easy reading.
Incorporate your brand colors and logo for instant recognition.
Include a clear call to action (CTA) on both sides.
Add a tear-off section at the bottom with your contact information for
convenience.
Use high-quality images or graphics related to electrical work to catch
the eye.
This door hanger design and copy aim to attract residential clients by
highlighting the benefits of your electrical services, special offers, and
how they can easily get in touch with you for their electrical needs.
The door knocker template will have three of the same design on front and three of the same design on the back. This template is from the print shop.

```html
<!DOCTYPE html>
<html lang="en">
<head>
<meta charset="utf-8">
<title>K&amp;T Electric Door Hanger</title>
<link href="https://fonts.googleapis.com/css2?family=Poppins:wght@400;500;600;700;800&family=Roboto:wght@400&display=swap" rel="stylesheet">
<style>
  :root{
    --bg:#a7aaae;
    --red:#dc2027;
    --black:#0b0b0b;
    --white:#ffffff;
    --rule:#2a2a2a;
  }
  *{box-sizing:border-box;margin:0;padding:0}
  html,body{width:1200px;height:1200px;overflow:hidden;background:var(--bg)}
  body{position:relative;font-family:"Poppins",sans-serif;color:var(--black)}
  .hanger{position:absolute;top:122px;width:404px;height:938px;background:var(--white);box-shadow:2px 3px 6px rgba(0,0,0,.25);overflow:hidden}
  .hanger--front{left:165px}
  .hanger--back{left:642px}
  .hanger__top{position:absolute;left:0;top:0;width:404px;height:340px;display:block}
  .brand{position:absolute;left:0;right:0;top:248px;text-align:center}
  .brand__name{font-weight:700;font-size:38px;line-height:1;letter-spacing:1px;color:var(--black)}
  .brand__sub{font-weight:500;font-size:11px;letter-spacing:.5px;margin-top:4px}
  .headline{position:absolute;left:0;right:0;text-align:center;font-weight:800;line-height:1}
  .headline--red{top:334px;font-size:37px;color:var(--red)}
  .headline--black{top:372px;font-size:45px;color:var(--black);letter-spacing:.5px}
  .tagline{position:absolute;left:24px;width:355px;top:422px;height:56px;background:var(--red);border-radius:7px;color:var(--white);font-size:19.5px;line-height:26px;text-align:center;padding-top:2px}
  .perks{position:absolute;left:32px;top:490px;list-style:none}
  .perks li{display:flex;align-items:center;height:37.3px;font-size:25.5px;font-weight:400}
  .perks svg{width:23px;height:23px;margin-right:12px;flex:none}
  .coupon{position:absolute;left:24px;top:653px;width:355px;height:124px;border-radius:8px;overflow:hidden;background:var(--black)}
  .coupon__amount{position:absolute;left:0;right:0;top:8px;text-align:center;font-weight:800;font-size:60px;line-height:62px;color:var(--white);letter-spacing:-1px}
  .coupon__amount span{color:var(--red)}
  .coupon__band{position:absolute;left:0;top:0;width:355px;height:124px}
  .coupon__text{position:absolute;left:0;right:0;bottom:12px;text-align:center;font-weight:700;font-size:22px;color:var(--white)}
  .coupon__dash{position:absolute;inset:4px;border:1.5px dashed var(--white);border-radius:6px}
  .intro{position:absolute;top:342px;left:0;right:0;text-align:center;font-weight:700;font-size:24px;line-height:25px}
  .intro span{display:block;color:var(--red)}
  .summary{position:absolute;left:17px;width:369px;top:392px;height:68px;background:var(--black);border-radius:10px;color:var(--white);font-size:15.5px;line-height:20px;text-align:center;padding-top:5px}
  .services{position:absolute;left:32px;width:346px;top:475px;list-style:none;font-family:"Roboto",sans-serif}
  .services li{height:31.3px;line-height:30px;text-align:center;font-size:19.5px;border-bottom:1px solid var(--rule)}
  .services li:last-child{border-bottom:none}
  .cta{position:absolute;left:0;top:801px;width:404px;height:84px;background:linear-gradient(90deg,#0b0b0b 0%,#3a3a3a 50%,#0b0b0b 100%)}
  .cta__tab{position:absolute;left:115px;top:-8px;width:173px;height:31px;background:var(--red);border-radius:5px 5px 8px 8px;color:var(--white);font-weight:700;font-size:18px;line-height:31px;text-align:center}
  .cta__phone{position:absolute;left:0;right:0;top:34px;display:flex;justify-content:center;align-items:center;color:var(--white);font-weight:600;font-size:37px;line-height:1}
  .cta__phone svg{width:42px;height:42px;margin-right:8px}
  .web{position:absolute;left:0;right:0;top:896px;display:flex;align-items:center;justify-content:center;gap:12px}
  .web__pill{background:var(--red);color:var(--white);border:2px solid var(--black);border-radius:14px;font-size:17px;line-height:22px;padding:1px 10px}
  .web__url{display:flex;align-items:center;font-size:19.5px}
  .web__url svg{width:15px;height:15px;margin-right:5px}
</style>
</head>
<body>

<!-- Front side -->
<section class="hanger hanger--front">
  <svg class="hanger__top" viewBox="0 0 404 340">
    <defs>
      <linearGradient id="cityTones" x1="0" y1="0" x2="0" y2="1">
        <stop offset="0" stop-color="#2f66c4"/>
        <stop offset=".45" stop-color="#3a5fa8"/>
        <stop offset=".8" stop-color="#5a5468"/>
        <stop offset="1" stop-color="#7a5a3c"/>
      </linearGradient>
    </defs>
    <rect width="404" height="340" fill="url(#cityTones)" role="img" aria-label="Night skyline of a city with lit office towers"/>
    <line x1="75" y1="-5" x2="202" y2="125" stroke="var(--bg)" stroke-width="6"/>
    <circle cx="202" cy="125" r="56" fill="var(--bg)"/>
    <polygon points="0,318 201,200 404,318 404,329 201,207 0,329" fill="var(--black)"/>
    <polygon points="0,296 125,238 125,252 0,329" fill="var(--red)"/>
    <polygon points="404,296 279,238 279,252 404,329" fill="var(--red)"/>
    <polygon points="0,329 201,207 404,329 404,340 0,340" fill="var(--white)"/>
  </svg>
  <div class="brand"><div class="brand__name">K&amp;T</div><div class="brand__sub">ELECTRIC, LLC</div></div>
  <h1 class="headline headline--red">NEED A RELIABLE</h1>
  <h1 class="headline headline--black">ELECTRICIAN?</h1>
  <p class="tagline">Your Local Electrical Expert is<br>Just Around the Corner!</p>
  <ul class="perks">
    <li><svg viewBox="0 0 24 24"><circle cx="12" cy="12" r="11" fill="var(--red)"/><path d="M7 12.5l3.2 3.2L17 9" fill="none" stroke="#fff" stroke-width="2.6" stroke-linecap="round" stroke-linejoin="round"/></svg>Quick Response Times</li>
    <li><svg viewBox="0 0 24 24"><circle cx="12" cy="12" r="11" fill="var(--red)"/><path d="M7 12.5l3.2 3.2L17 9" fill="none" stroke="#fff" stroke-width="2.6" stroke-linecap="round" stroke-linejoin="round"/></svg>Affordable Rates</li>
    <li><svg viewBox="0 0 24 24"><circle cx="12" cy="12" r="11" fill="var(--red)"/><path d="M7 12.5l3.2 3.2L17 9" fill="none" stroke="#fff" stroke-width="2.6" stroke-linecap="round" stroke-linejoin="round"/></svg>Quality Workmanship</li>
    <li><svg viewBox="0 0 24 24"><circle cx="12" cy="12" r="11" fill="var(--red)"/><path d="M7 12.5l3.2 3.2L17 9" fill="none" stroke="#fff" stroke-width="2.6" stroke-linecap="round" stroke-linejoin="round"/></svg>Fully Licensed &amp; Insured</li>
  </ul>
  <div class="coupon">
    <svg class="coupon__band" viewBox="0 0 355 124"><polygon points="0,66 177,82 355,66 355,124 0,124" fill="var(--red)"/><polygon points="327,2 353,2 353,28" fill="#d9d9d9"/></svg>
    <div class="coupon__amount">10<span>%</span> OFF</div>
    <div class="coupon__text">YOUR FIRST SERVICE CALL!</div>
    <div class="coupon__dash"></div>
  </div>
  <div class="cta">
    <div class="cta__tab">CALL US TODAY</div>
    <div class="cta__phone"><svg viewBox="0 0 42 42"><circle cx="21" cy="21" r="20" fill="var(--red)" stroke="#fff" stroke-width="2"/><path d="M14 11c2-1 3 0 4 2l1.5 3c.5 1 0 2-1 2.6l-1.2.8c1 2.6 3 4.7 5.6 5.8l.8-1.2c.6-1 1.6-1.4 2.6-1l3 1.5c2 1 3 2 2 4-1 2.4-3.5 3.4-6 2.6-6-2-10.5-6.5-12.5-12.5-.8-2.5.2-5 2.2-6z" fill="var(--black)"/></svg>(555) 318-6470</div>
  </div>
  <div class="web"><span class="web__pill">Visit Us</span><span class="web__url"><svg viewBox="0 0 16 16"><g fill="none" stroke="var(--red)" stroke-width="1.2"><circle cx="8" cy="8" r="6.5"/><ellipse cx="8" cy="8" rx="3" ry="6.5"/><line x1="1.5" y1="8" x2="14.5" y2="8"/><line x1="2.5" y1="4.8" x2="13.5" y2="4.8"/><line x1="2.5" y1="11.2" x2="13.5" y2="11.2"/></g></svg>www.kandtelectric.example</span></div>
</section>

<!-- Back side -->
<section class="hanger hanger--back">
  <svg class="hanger__top" viewBox="0 0 404 340">
    <defs>
      <radialGradient id="bulbTones" cx=".55" cy=".4" r=".7">
        <stop offset="0" stop-color="#c98a3a"/>
        <stop offset=".45" stop-color="#6b3a12"/>
        <stop offset="1" stop-color="#140804"/>
      </radialGradient>
    </defs>
    <rect width="404" height="340" fill="url(#bulbTones)" role="img" aria-label="Glowing filament light bulbs hanging against a dark background"/>
    <line x1="330" y1="-5" x2="202" y2="125" stroke="var(--bg)" stroke-width="6"/>
    <circle cx="202" cy="125" r="56" fill="var(--bg)"/>
    <polygon points="0,318 201,200 404,318 404,329 201,207 0,329" fill="var(--black)"/>
    <polygon points="0,296 125,238 125,252 0,329" fill="var(--red)"/>
    <polygon points="404,296 279,238 279,252 404,329" fill="var(--red)"/>
    <polygon points="0,329 201,207 404,329 404,340 0,340" fill="var(--white)"/>
  </svg>
  <div class="brand"><div class="brand__name">K&amp;T</div><div class="brand__sub">ELECTRIC, LLC</div></div>
  <h2 class="intro">Don't Let Electrical<span>Issues Keep You in the Dark!</span></h2>
  <p class="summary">From flickering lights to complete system<br>upgrades, we've got all your residential<br>electrical needs covered.</p>
  <ul class="services">
    <li>Electrical Repairs &amp; Troubleshooting</li>
    <li>Lighting Installation &amp; Upgrades</li>
    <li>Safety Inspections &amp; Code Compliance</li>
    <li>Energy-Efficient Solutions</li>
    <li>24/7 Emergency Services</li>
    <li>Why Choose Us?</li>
    <li>Friendly, Local Service</li>
    <li>Over 30 Years of Experience</li>
    <li>Satisfaction Guaranteed</li>
    <li>Upfront Pricing</li>
  </ul>
  <div class="cta">
    <div class="cta__tab">CALL US TODAY</div>
    <div class="cta__phone"><svg viewBox="0 0 42 42"><circle cx="21" cy="21" r="20" fill="var(--red)" stroke="#fff" stroke-width="2"/><path d="M14 11c2-1 3 0 4 2l1.5 3c.5 1 0 2-1 2.6l-1.2.8c1 2.6 3 4.7 5.6 5.8l.8-1.2c.6-1 1.6-1.4 2.6-1l3 1.5c2 1 3 2 2 4-1 2.4-3.5 3.4-6 2.6-6-2-10.5-6.5-12.5-12.5-.8-2.5.2-5 2.2-6z" fill="var(--black)"/></svg>(555) 318-6470</div>
  </div>
  <div class="web"><span class="web__pill">Visit Us</span><span class="web__url"><svg viewBox="0 0 16 16"><g fill="none" stroke="var(--red)" stroke-width="1.2"><circle cx="8" cy="8" r="6.5"/><ellipse cx="8" cy="8" rx="3" ry="6.5"/><line x1="1.5" y1="8" x2="14.5" y2="8"/><line x1="2.5" y1="4.8" x2="13.5" y2="4.8"/><line x1="2.5" y1="11.2" x2="13.5" y2="11.2"/></g></svg>www.kandtelectric.example</span></div>
</section>

</body>
</html>
```